Tallow Home Buyers

We need a website designed for the a house buying company. It can look and feel similar to a real estate agency, but the messaging is different. Attached in the document below you will see what we are looking for. The main thing we are going for is clean, corporate and approachable. The Logo files are also attached. We want to use the logo and branding throughout the site.

```html
<!DOCTYPE html>
<html lang="en">
<head>
<meta charset="utf-8">
<title>Tallow Home Buyers</title>
<link href="https://fonts.googleapis.com/css2?family=Hind:wght@500;600;700&family=Lato:wght@400;700&display=swap" rel="stylesheet">
<style>
:root{
  --blue:#0d4c97;
  --blue-dark:#0a3d7a;
  --green:#6aab2b;
  --mint:#eaf7f3;
  --soft:#e6ecf4;
  --ink:#222;
  --muted:#6b6b6b;
  --black:#111;
  --footer:#1c1c1c;
  --white:#fff;
}
*{box-sizing:border-box;margin:0;padding:0}
html,body{width:1200px;height:4313px;overflow:hidden}
body{position:relative;font-family:"Lato",sans-serif;color:var(--ink);background:var(--white)}
.abs{position:absolute}
h1,h2,h3,.heading{font-family:"Hind",sans-serif}
.center{text-align:center}

.topbar{left:0;top:0;width:1200px;height:45px;background:var(--black);color:#ddd;font-size:12px}
.topbar .mail{left:160px;top:14px;display:flex;gap:10px;align-items:center}
.topbar .phone{left:916px;top:14px;display:flex;gap:10px;align-items:center}

.nav{left:0;top:45px;width:1200px;height:75px;background:var(--mint)}
.logo{font-family:"Hind",sans-serif;font-weight:700;color:var(--blue);line-height:1}
.nav .logo{left:160px;top:8px;font-size:30px;width:180px}
.nav .logo small{display:block;font-size:15px;letter-spacing:3px;margin-top:2px}
.menu{left:438px;top:22px;display:flex;font-size:12px}
.menu a{color:#222;text-decoration:none;padding:8px 11px;border:1px solid transparent}
.menu a.active{border-color:var(--blue);color:var(--blue);background:#fff}

.hero{left:0;top:120px;width:1200px;height:637px;background:linear-gradient(180deg,#c95a6c 0%,#7a4a6a 28%,#2e2f3a 55%,#3a3a3c 80%,#4a4a4a 100%)}
.hero-box{left:160px;top:251px;width:638px;height:389px;background:rgba(20,20,20,.82)}
.hero-box h1{position:absolute;left:34px;top:38px;color:#fff;font-size:56px;line-height:1.08;font-weight:700;text-transform:uppercase}
.hero-input{left:192px;top:439px;width:524px;height:51px;background:#fff;border:1px solid #ccc;display:flex;align-items:center;padding-left:16px;gap:12px;font-size:15px;color:#555}
.hero-btn{left:192px;top:520px;width:186px;height:53px;background:var(--blue);color:#fff;font-weight:700;font-size:16px;display:flex;align-items:center;justify-content:center}
.slide-nav{left:895px;top:630px;width:305px;height:127px;background:rgba(0,0,0,.55)}
.slide-ctrl{position:absolute;width:44px;height:44px;border-radius:50%;background:#fff;display:flex;align-items:center;justify-content:center}
.slide-label{position:absolute;color:#fff;font-size:10px;font-weight:700;letter-spacing:.5px}

.reasons{left:0;top:757px;width:1200px;height:637px;background:var(--soft)}
.sec-title{position:absolute;left:0;width:1200px;text-align:center;font-family:"Hind",sans-serif;font-weight:700;font-size:42px;color:var(--blue);text-transform:uppercase;line-height:1}
.sub{position:absolute;left:270px;width:660px;text-align:center;font-size:11px;line-height:19px;color:#444}
.card{position:absolute;width:203px;height:136px;background:#fff;border-radius:4px;box-shadow:0 1px 3px rgba(0,0,0,.08);text-align:center;padding:14px 10px 0}
.card h3{font-size:14px;color:var(--blue);font-weight:700;margin-bottom:6px}
.card p{font-size:10.5px;line-height:19.5px;color:#666}
.btn-blue{position:absolute;background:var(--blue);color:#fff;font-weight:700;font-size:13px;display:flex;align-items:center;justify-content:center}

.feature{position:absolute;width:200px;text-align:center}
.feature .ic{width:90px;height:90px;margin:0 auto;border-radius:50%;background:var(--green);display:flex;align-items:center;justify-content:center;box-shadow:inset -8px -8px 0 rgba(0,0,0,.12)}
.feature h3{font-size:15px;font-weight:700;color:#222;margin-top:12px;font-family:"Lato",sans-serif}
.feature p{font-size:11px;line-height:19.5px;color:#777;margin-top:6px}
.house{left:594px;top:1557px;width:606px;height:410px;background:linear-gradient(180deg,#ffffff 0%,#c9d6ea 18%,#8fa9d2 55%,#7e97c0 80%,#eef1f5 100%)}

.how{left:0;top:2031px;width:1200px;height:375px;background:linear-gradient(180deg,#2b2b2b,#1e2226 60%,#2a2f33)}
.step{position:absolute;width:180px;text-align:center;color:#fff;font-size:12px;font-weight:700;line-height:18px}
.step .ic{width:80px;height:80px;margin:0 auto 10px;border-radius:50%;background:#fff;display:flex;align-items:center;justify-content:center;border:3px solid rgba(255,255,255,.3)}

.cta{left:0;top:2406px;width:1200px;height:189px;background:var(--blue)}
.cta h2{position:absolute;left:0;top:47px;width:1200px;text-align:center;color:var(--green);font-size:38px;font-weight:700}
.btn-white{position:absolute;background:#fff;color:var(--green);font-weight:700;font-size:13px;display:flex;align-items:center;justify-content:center}

.frame{left:0;top:2648px;width:226px;height:412px;border:12px solid var(--blue)}
.video{left:37px;top:2685px;width:502px;height:335px;background:linear-gradient(180deg,#4d5358,#2f3437 55%,#3d4236)}
.play{left:255px;top:2819px;width:66px;height:66px;border-radius:50%;background:var(--green);box-shadow:0 0 0 8px rgba(106,171,43,.35);display:flex;align-items:center;justify-content:center}
.green-title{position:absolute;font-family:"Hind",sans-serif;font-weight:700;color:var(--green);font-size:40px;line-height:1}
.faq-item{position:absolute;left:611px;width:427px;background:#ebebeb}
.faq-q{font-size:12px;font-weight:700;color:#222;padding:13px 14px}
.faq-a{font-size:10.5px;line-height:19px;color:#888;padding:0 14px 10px}

.t-card{left:293px;top:3226px;width:614px;height:176px;background:#fff;box-shadow:0 2px 8px rgba(0,0,0,.1);text-align:center}
.t-under{left:326px;top:3402px;width:548px;height:12px;background:#ececec}
.avatar{left:559px;top:3187px;width:80px;height:80px;border-radius:50%;background:linear-gradient(180deg,#c9ccd0,#6b7480);border:4px solid var(--green)}
.t-name{position:absolute;left:0;width:614px;top:50px;font-size:11px;color:var(--blue)}
.t-head{position:absolute;left:0;width:614px;top:72px;font-size:11px;font-weight:700}
.t-text{position:absolute;left:20px;width:574px;top:92px;font-size:11px;line-height:20px;color:#555}
.dots{position:absolute;left:0;width:614px;top:142px;display:flex;justify-content:center;gap:14px}

.field{position:absolute;height:37px;border:1px solid #ccc;background:#fff;font-size:11px;color:#666;padding:11px 10px}

.loc{left:0;top:3869px;width:1200px;height:112px;background:var(--blue)}
.loc h2{position:absolute;left:162px;top:38px;color:#fff;font-size:31px;font-weight:700}
.btn-outline{position:absolute;left:854px;top:38px;width:142px;height:37px;border:1px solid #fff;color:#fff;font-size:13px;font-weight:700;display:flex;align-items:center;justify-content:center}

.footer{left:0;top:3981px;width:1200px;height:332px;background:var(--footer);color:#ddd}
.footer .logo{position:absolute;left:162px;top:46px;font-size:30px}
.footer .logo small{display:block;font-size:15px;letter-spacing:3px;margin-top:2px}
.f-about{position:absolute;left:162px;top:128px;width:200px;font-size:11px;line-height:19.5px;color:#ddd}
.f-head{position:absolute;top:45px;font-size:12px;font-weight:700;color:#2f6fbf;text-transform:uppercase}
.f-links{position:absolute;left:387px;top:88px;font-size:11px;line-height:24px}
.f-contact{position:absolute;left:613px;font-size:11px;display:flex;gap:14px;align-items:flex-start;line-height:22px}
.social{position:absolute;top:94px;width:40px;height:40px;border-radius:50%;background:#2c5fa8}
.find-btn{position:absolute;left:837px;top:155px;width:201px;height:41px;background:var(--blue);color:#fff;font-size:12px;font-weight:700;display:flex;align-items:center}
.find-btn span{flex:1;padding-left:24px}
.find-btn i{width:41px;height:41px;background:#fff;display:flex;align-items:center;justify-content:center}
.f-rule{position:absolute;left:0;top:280px;width:1200px;height:1px;background:#333}
.copy{position:absolute;left:0;width:1200px;top:300px;text-align:center;font-size:11px;color:#ccc}
</style>
</head>
<body>

<div class="abs topbar">
  <div class="abs mail">
    <svg width="18" height="13" viewBox="0 0 18 13"><rect x="0.5" y="0.5" width="17" height="12" fill="none" stroke="#6aab2b"/><path d="M1 1l8 6 8-6" fill="none" stroke="#6aab2b"/></svg>
    <span>support@tallowhomebuyers.com</span>
  </div>
  <div class="abs phone">
    <svg width="18" height="18" viewBox="0 0 24 24"><path d="M6 2l4 4-2 3c1 3 4 6 7 7l3-2 4 4-3 4C10 21 3 14 2 5z" fill="#6aab2b"/></svg>
    <span>(555) 014-2288</span>
  </div>
</div>

<header class="abs nav">
  <div class="abs logo">TALLOW<small>HOME BUYERS</small></div>
  <nav class="abs menu">
    <a class="active">Home</a><a>Why Tallow Home Buyers</a><a>How It Works</a><a>Reasons to Sell</a><a>Locations</a><a>FAQ</a><a>Contact Us</a>
  </nav>
</header>

<section class="abs hero" role="img" aria-label="Photo of a modern two-storey house at dusk under a pink sky"></section>
<div class="abs hero-box"><h1>We buy homes from<br>people in a pinch!</h1></div>
<div class="abs hero-input">
  <svg width="14" height="20" viewBox="0 0 14 20"><path d="M7 0a7 7 0 0 1 7 7c0 5-7 13-7 13S0 12 0 7a7 7 0 0 1 7-7z" fill="#555"/><circle cx="7" cy="7" r="2.6" fill="#fff"/></svg>
  <span>Enter Your Street Address:</span>
</div>
<div class="abs hero-btn">Get your cash Offer</div>
<div class="abs slide-nav">
  <div class="slide-ctrl" style="left:32px;top:14px"><svg width="14" height="22"><path d="M11 2L3 11l8 9" fill="none" stroke="#333" stroke-width="2"/></svg></div>
  <div class="slide-label" style="left:132px;top:20px">PREV</div>
  <div style="position:absolute;left:132px;top:46px;width:70px;height:1px;background:#fff"></div>
  <div class="slide-label" style="left:149px;top:78px">NEXT</div>
  <div style="position:absolute;left:90px;top:66px;width:110px;height:1px;background:#fff"></div>
  <div class="slide-ctrl" style="left:226px;top:51px"><svg width="14" height="22"><path d="M3 2l8 9-8 9" fill="none" stroke="#333" stroke-width="2"/></svg></div>
</div>

<section class="abs reasons"></section>
<h2 class="sec-title" style="top:824px">Reason to Sell</h2>
<p class="sub" style="top:874px">No matter your situation, we will buy your home. No need to worry about the condition of the house either - we'll make this a stress-free process and get you cash quickly.</p>

<div class="card" style="left:160px;top:951px"><h3>Retirement</h3><p>Lorem Ipsum is simply dummy text of the printing and typesetting industry. Lorem Ipsum has been the industry's standard.</p></div>
<div class="card" style="left:386px;top:951px"><h3>Downsizing or Upsizing</h3><p>Lorem Ipsum is simply dummy text of the printing and typesetting industry. Lorem Ipsum has been the industry's standard.</p></div>
<div class="card" style="left:611px;top:951px"><h3>Inheritance</h3><p>Have you inherited a home and you don't want to worry about the headache that comes with it? Sell it to the Tallow Home Experts!</p></div>
<div class="card" style="left:835px;top:951px"><h3>Massive Repairs</h3><p>Is your home too much to manage? No problem; our team is happy to take it off your hands.</p></div>
<div class="card" style="left:160px;top:1108px"><h3>Bad Mortgage</h3><p>Selling your home is a great way to get out of your current mortgage quick.</p></div>
<div class="card" style="left:386px;top:1108px"><h3>Moving</h3><p>Sometimes you just want to move and that's okay too! Let us help you get into your dream home.</p></div>
<div class="card" style="left:611px;top:1108px"><h3>Probate</h3><p>Lorem Ipsum is simply dummy text of the printing and typesetting industry. Lorem Ipsum has been the industry's standard dummy tex.</p></div>
<div class="card" style="left:835px;top:1108px"><h3>Divorce</h3><p>Lorem Ipsum is simply dummy text of the printing and typesetting industry. Lorem Ipsum has been the industry's standard.</p></div>
<div class="btn-blue" style="left:522px;top:1286px;width:156px;height:42px">More Reasons to Sell</div>

<h2 class="sec-title" style="top:1468px">Why Tallow Home Buyers?</h2>
<div class="feature" style="left:163px;top:1559px">
  <div class="ic"><svg width="40" height="40" viewBox="0 0 40 40"><rect x="6" y="6" width="28" height="28" rx="3" fill="none" stroke="#fff" stroke-width="3"/><path d="M14 26l12-12M18 14h8v8" fill="none" stroke="#fff" stroke-width="3"/></svg></div>
  <h3>Quick Turnaround</h3><p>Lorem Ipsum is simply dummy text of the printing and typesetting industry.</p>
</div>
<div class="feature" style="left:387px;top:1559px">
  <div class="ic"><svg width="40" height="40" viewBox="0 0 40 40"><rect x="10" y="4" width="20" height="16" rx="2" fill="none" stroke="#fff" stroke-width="3"/><text x="20" y="17" text-anchor="middle" fill="#fff" font-size="12" font-family="Lato" font-weight="700">$</text><circle cx="13" cy="32" r="4" fill="none" stroke="#fff" stroke-width="3"/><circle cx="27" cy="32" r="4" fill="none" stroke="#fff" stroke-width="3"/><path d="M15 28l10-8M25 28L15 20" stroke="#fff" stroke-width="3"/></svg></div>
  <h3>Zero Fees</h3><p>Lorem Ipsum is simply dummy text of the printing and typesetting industry.</p>
</div>
<div class="feature" style="left:163px;top:1781px">
  <div class="ic"><svg width="40" height="40" viewBox="0 0 40 40"><rect x="10" y="6" width="24" height="20" fill="none" stroke="#fff" stroke-width="3"/><circle cx="19" cy="14" r="2" fill="#fff"/><circle cx="26" cy="14" r="2" fill="#fff"/><circle cx="10" cy="30" r="4" fill="none" stroke="#fff" stroke-width="3"/><path d="M14 30h16v4" fill="none" stroke="#fff" stroke-width="3"/></svg></div>
  <h3>Stress &amp; Hassle Free</h3><p>Lorem Ipsum is simply dummy text of the printing and typesetting industry.</p>
</div>
<div class="feature" style="left:387px;top:1781px">
  <div class="ic"><svg width="44" height="40" viewBox="0 0 44 40"><path d="M10 8h28l-4 20H6z" fill="none" stroke="#fff" stroke-width="3"/><text x="22" y="24" text-anchor="middle" fill="#fff" font-size="14" font-family="Lato" font-weight="700">$</text><path d="M4 32h30" stroke="#fff" stroke-width="3"/></svg></div>
  <h3>Cold Hard Cash Fast</h3><p>Lorem Ipsum is simply dummy text of the printing and typesetting industry.</p>
</div>
<div class="abs house" role="img" aria-label="Illustration of a blue two-storey house with a garage"></div>

<section class="abs how" role="img" aria-label="Dim background photo of a house at night"></section>
<h2 class="sec-title" style="top:2099px;color:#fff">How Its Work</h2>
<svg class="abs" style="left:240px;top:2180px" width="730" height="120" viewBox="0 0 730 120">
  <path d="M0 50C60 110 120 110 182 90C240 20 300 10 358 46C420 110 480 110 543 90C600 20 660 10 724 46" fill="none" stroke="#bbb" stroke-width="1.5" stroke-dasharray="2 4"/>
</svg>
<div class="step" style="left:149px;top:2186px">
  <div class="ic"><svg width="40" height="40" viewBox="0 0 24 24"><path d="M6 2l4 4-2 3c1 3 4 6 7 7l3-2 4 4-3 4C10 21 3 14 2 5z" fill="none" stroke="#0d4c97" stroke-width="2"/><text x="16" y="10" text-anchor="middle" fill="#0d4c97" font-size="9" font-family="Lato" font-weight="700">@</text></svg></div>
  Call or Email Us
</div>
<div class="step" style="left:332px;top:2227px">
  <div class="ic"><svg width="40" height="40" viewBox="0 0 40 40"><path d="M20 6a14 12 0 1 1-8 22l-6 4 2-7A14 12 0 0 1 20 6z" fill="none" stroke="#0d4c97" stroke-width="2.5"/><path d="M20 12l2.5 5 5.5.8-4 3.8 1 5.4-5-2.6-5 2.6 1-5.4-4-3.8 5.5-.8z" fill="none" stroke="#0d4c97" stroke-width="2"/></svg></div>
  Speak to a Tallow Expert
</div>
<div class="step" style="left:508px;top:2186px">
  <div class="ic"><svg width="40" height="40" viewBox="0 0 40 40"><rect x="6" y="8" width="28" height="26" fill="none" stroke="#0d4c97" stroke-width="2.5"/><path d="M6 15h28M13 5v6M27 5v6M11 20h4M18 20h4M25 20h4M11 26h4M18 26h4M25 26h4" stroke="#0d4c97" stroke-width="2.5"/></svg></div>
  Schedule a Quick<br>Walk-Through
</div>
<div class="step" style="left:693px;top:2227px">
  <div class="ic"><svg width="42" height="40" viewBox="0 0 42 40"><rect x="14" y="8" width="22" height="12" fill="none" stroke="#0d4c97" stroke-width="2.5"/><text x="25" y="18" text-anchor="middle" fill="#0d4c97" font-size="10" font-family="Lato" font-weight="700">$</text><path d="M4 24h8l8 4h10l-6 6H4z" fill="#0d4c97"/></svg></div>
  Receive a Cash Offer
</div>
<div class="step" style="left:874px;top:2186px">
  <div class="ic"><svg width="40" height="40" viewBox="0 0 40 40"><rect x="6" y="6" width="28" height="14" rx="2" fill="none" stroke="#0d4c97" stroke-width="2.5"/><circle cx="20" cy="13" r="3" fill="#0d4c97"/><rect x="14" y="22" width="18" height="14" rx="2" fill="#0d4c97"/><text x="23" y="33" text-anchor="middle" fill="#fff" font-size="10" font-family="Lato" font-weight="700">$</text></svg></div>
  Get Paid
</div>

<section class="abs cta">
  <h2>We’re the experts you turn to in a pinch</h2>
  <div class="btn-white" style="left:544px;top:115px;width:111px;height:37px">Get Started</div>
</section>

<div class="abs frame"></div>
<div class="abs video" role="img" aria-label="Video still of a large two-storey house surrounded by trees"></div>
<div class="abs play"><svg width="16" height="18"><path d="M2 1l13 8-13 8z" fill="#fff"/></svg></div>
<h2 class="green-title" style="left:613px;top:2647px">FAQ</h2>
<div class="faq-item" style="top:2725px;height:126px">
  <div class="faq-q">How fast does this work?</div>
  <div class="faq-a" style="padding-top:6px">Lorem Ipsum is simply dummy text of the printing and typesetting industry. Lorem Ipsum has been the industry's standard dummy text ever since the 1500s.</div>
</div>
<div class="faq-item" style="top:2869px;height:42px"><div class="faq-q">What are your fees?</div></div>
<div class="faq-item" style="top:2928px;height:43px"><div class="faq-q">What if my home is not in good shape?</div></div>
<div class="btn-blue" style="left:611px;top:3013px;width:112px;height:39px">View More</div>

<h2 class="green-title" style="left:0;width:1200px;text-align:center;top:3126px;font-size:38px">Our Testimonials</h2>
<div class="abs t-under"></div>
<div class="abs t-card">
  <div class="t-name">- Dana</div>
  <div class="t-head">“Smooth, easy, fast.”</div>
  <div class="t-text">I was hesitant of the whole deal, because it seemed too easy. And now that I'm at the final sale, if Marcus tells you he's doing it, he's doing it. It's that simple.”</div>
  <div class="dots">
    <svg width="10" height="10"><path d="M5 1l4 4-4 4-4-4z" fill="none" stroke="#6aab2b"/></svg>
    <svg width="10" height="10"><path d="M5 1l4 4-4 4-4-4z" fill="#6aab2b"/></svg>
    <svg width="10" height="10"><path d="M5 1l4 4-4 4-4-4z" fill="none" stroke="#6aab2b"/></svg>
  </div>
</div>
<div class="abs avatar" role="img" aria-label="Customer portrait photo"></div>

<h2 class="green-title" style="left:0;width:1200px;text-align:center;top:3494px;font-size:38px">Contact Us</h2>
<div class="field" style="left:270px;top:3574px;width:209px">Name:</div>
<div class="field" style="left:495px;top:3574px;width:210px">Email:</div>
<div class="field" style="left:720px;top:3574px;width:209px">Phone:</div>
<div class="field" style="left:270px;top:3626px;width:209px">City:</div>
<div class="field" style="left:495px;top:3626px;width:210px">State:</div>
<div class="field" style="left:720px;top:3626px;width:209px">Zip:</div>
<div class="field" style="left:270px;top:3678px;width:659px;height:59px">Address:</div>
<div class="btn-blue" style="left:544px;top:3768px;width:112px;height:37px">Submit</div>

<section class="abs loc">
  <h2>Find our all locations on City Map !</h2>
  <div class="btn-outline">View All Location</div>
</section>

<footer class="abs footer">
  <div class="logo" style="color:#1f6fd1">TALLOW<small>HOME BUYERS</small></div>
  <p class="f-about">Lorem Ipsum is simply dummy text of the printing and typesetting industry. Lorem Ipsum has been the industry's standard dummy text ever since the 1500s.</p>

  <div class="f-head" style="left:387px">Sitemap</div>
  <div class="f-links">Home<br>How Its Work<br>Why us?<br>Reason to sell<br>Testimonials<br>FAQ<br>Contact Us</div>

  <div class="f-head" style="left:613px">Contact Info</div>
  <div class="f-contact" style="top:90px"><svg width="18" height="18" viewBox="0 0 24 24"><path d="M6 2l4 4-2 3c1 3 4 6 7 7l3-2 4 4-3 4C10 21 3 14 2 5z" fill="#2f6fbf"/></svg><span>+1- (555) 014-2288</span></div>
  <div class="f-contact" style="top:128px"><svg width="18" height="13" viewBox="0 0 18 13"><rect width="18" height="13" fill="#2f6fbf"/><path d="M1 1l8 6 8-6" fill="none" stroke="#1c1c1c"/></svg><span>support@tallowhomebuyers.com</span></div>
  <div class="f-contact" style="top:165px"><svg width="14" height="20" viewBox="0 0 14 20"><path d="M7 0a7 7 0 0 1 7 7c0 5-7 13-7 13S0 12 0 7a7 7 0 0 1 7-7z" fill="#2f6fbf"/><circle cx="7" cy="7" r="2.6" fill="#1c1c1c"/></svg><span>100- Lorem ipsum is simply<br>dummy text.</span></div>

  <div class="f-head" style="left:837px">Follow us on</div>
  <div class="social" style="left:834px"></div>
  <div class="social" style="left:887px"></div>
  <div class="social" style="left:939px"></div>
  <div class="social" style="left:993px"></div>
  <div class="find-btn"><span>Find our locations</span><i><svg width="26" height="16"><path d="M1 8h22M16 1l7 7-7 7" fill="none" stroke="#0d4c97" stroke-width="2"/></svg></i></div>

  <div class="f-rule"></div>
  <p class="copy">Copyright © <b>TallowHomeBuyers</b> 2019. Terms &amp; Conditions | Privacy Policy.</p>
</footer>

</body>
</html>
```